Digital Album Cover - Frosted Lanterns (Night Falls Still)

HiI need a digital album cover for a piano instrumental cover single

Artist: Corey Dalton
Title: Frosted Lanterns (Night Falls Still)

The song was originally by Derek Holloway

Please use my logo

You can listen to the track herehttps://soundcloud.com/coreydaltonkeys/frosted-lanterns-night-falls-still-piano-instrumental-cover

Requirements
Must have
• My logo design Corey Dalton

```html
<!DOCTYPE html>
<html lang="en">
<head>
<meta charset="utf-8">
<title>Frosted Lanterns (Night Falls Still) – Corey Dalton</title>
<link rel="stylesheet" href="https://fonts.googleapis.com/css2?family=Special+Elite&family=Montserrat:wght@500&family=Tinos:wght@700&display=swap">
<style>
  :root {
    --ink-black: #0b0b0b;
    --deep-grey: #2a2a2a;
    --key-white: #e9e9e9;
    --text-white: #ffffff;
    --badge-white: #ffffff;
    --tagline-grey: #e4e4e4;
  }
  html, body {
    margin: 0;
    padding: 0;
    width: 1200px;
    height: 1200px;
    overflow: hidden;
    background: var(--ink-black);
  }
  .cover {
    position: relative;
    width: 1200px;
    height: 1200px;
    overflow: hidden;
  }
  .cover-photo {
    position: absolute;
    inset: 0;
    background:
      radial-gradient(ellipse 90px 320px at 620px 260px, rgba(255,255,255,0.32), transparent 70%),
      linear-gradient(100deg, var(--key-white) 0%, #c4c4c4 20%, #5a5a5a 33%, var(--ink-black) 55%, var(--deep-grey) 100%),
      var(--ink-black);
  }
  .cover-photo::after {
    content: "";
    position: absolute;
    inset: 0;
    background: linear-gradient(180deg, rgba(0,0,0,0.78) 0%, rgba(0,0,0,0.25) 45%, rgba(0,0,0,0) 100%);
  }
  .track-title {
    position: absolute;
    top: 290px;
    left: 0;
    width: 1200px;
    margin: 0;
    text-align: center;
    font-family: "Special Elite", "Courier New", monospace;
    font-weight: 400;
    font-size: 48px;
    line-height: 1;
    color: var(--text-white);
    white-space: nowrap;
  }
  .brand-badge {
    position: absolute;
    left: 57px;
    top: 690px;
    width: 264px;
    height: 264px;
    border-radius: 50%;
    background: var(--badge-white);
  }
  .brand-name {
    position: absolute;
    left: 354px;
    top: 773px;
    margin: 0;
    font-family: "Montserrat", Arial, sans-serif;
    font-weight: 500;
    font-size: 98px;
    letter-spacing: -1px;
    line-height: 1;
    color: var(--text-white);
    white-space: nowrap;
  }
  .brand-tagline {
    position: absolute;
    left: 454px;
    top: 892px;
    margin: 0;
    font-family: "Montserrat", Arial, sans-serif;
    font-weight: 500;
    font-size: 49px;
    line-height: 1;
    color: var(--tagline-grey);
    white-space: nowrap;
  }
  .credit-line {
    position: absolute;
    left: 492px;
    margin: 0;
    font-family: "Tinos", "Times New Roman", serif;
    font-weight: 700;
    font-size: 85px;
    line-height: 1;
    color: var(--text-white);
    white-space: nowrap;
  }
  .credit-by { top: 966px; }
  .credit-name { top: 1090px; left: 486px; }
</style>
</head>
<body>
  <main class="cover">
    <div class="cover-photo" role="img" aria-label="Black and white close-up photograph of piano keys receding into soft blurred darkness"></div>

    <h1 class="track-title">Frosted Lanterns (Night Falls Still)</h1>

    <div class="brand-badge"></div>
    <p class="brand-name">COREY DALTON</p>
    <p class="brand-tagline">Wedding &amp; Event Pianist</p>

    <p class="credit-line credit-by">BY</p>
    <p class="credit-line credit-name">Derek</p>
  </main>
</body>
</html>
```